TB - WESITE NEEDED PAGE: Clean / Modern / Pro & Dynamic

Tavlin-Brokers is a new insurance brokerage firm dealing exclusively with companies (BToB) providing the following property: Liabilities Insurance Insurances Automobile Insurance Insurances Construction% 26amp; Engineering Casualty Workmen 's Compensation Health Insurance Marime% 26amp; Transit Credit Insurance Young, Fast, Proactive and Dynamic we call ourselves Tavlin-Brokers because we are a "start-up" willing to make a difference in the market, bringing modernity and speed to our industry, still too bureaucratic / procedural / opaque uninitiated. We need something respecting the colors of our orange logtype; blue; white; black; easy to scroll, with simple information on the company; - who we are - our team (with the pictures) - what we do - what we do - contact us, contact us (google map) Luanda (Angola) Small company, just need something flashy / professional / structured / modern.

Target Market(s)

BtoB; Oil and gas companies; French speaking copying established in Angola, all industrials, factories and importers of goods.

Industry/Entity Type

Insurance Broker

Font styles to use
Sans Serif

Colors

Designer to choose colors to be used in the design.

Requirements
Must have
• We need something respecting the colors of our orange logtype; blue; white; black; easy to scroll, with simple information on the company; - who we are - our team (with the pictures) - what we do - what we do - contact us, contact us (google map) Luanda (Angola) Small company, just need something flashy / professional / structured / modern.
Nice to have
• A page format
Should not have
• WE DO NOT WANT A REFER TO OUR LOGO, but a Home Page for our Website with the basics categories ... >> PLEASE CAREFULLY USE THE RIGHT COLOR OF THE LOGOTYPE which are the ones enclosed Orange / Turquoise / Black as per the business card .

```html
<!DOCTYPE html>
<html lang="en">
<head>
<meta charset="utf-8">
<title>Tavlin-Brokers — Insurance Brokerage Firm</title>
<link rel="stylesheet" href="https://fonts.googleapis.com/css2?family=Lato:wght@300;400;700&display=swap">
<style>
:root{
  --orange:#f0522a;
  --orange-soft:#ee7c5c;
  --blue:#4ea9da;
  --ink:#2b2b2b;
  --text:#555;
  --muted:#9a9a9a;
  --line:#dcdcdc;
  --field:#f4f4f4;
  --footer:#2f2f2f;
  --footer-text:#8a8a8a;
  --white:#fff;
}
*{box-sizing:border-box;margin:0;padding:0}
html,body{width:1200px;height:3393px;overflow:hidden}
body{font-family:'Lato',sans-serif;color:var(--ink);background:var(--white);position:relative}
.abs{position:absolute}
.btn{position:absolute;display:flex;align-items:center;justify-content:center;background:var(--orange);color:var(--white);border-radius:40px;font-weight:700;text-decoration:none}

/* header */
.site-header{position:absolute;top:0;left:0;width:1200px;height:82px;background:var(--white);z-index:2}
.brand{position:absolute;left:72px;top:28px;display:flex;align-items:center;gap:8px;font-weight:700;font-size:14px;color:var(--orange);text-transform:uppercase}
.brand-dot{width:22px;height:22px;border-radius:50%;background:var(--orange)}
.main-nav a{position:absolute;top:32px;font-size:15px;color:var(--ink);text-decoration:none}
.nav-cta{left:957px;top:22px;width:169px;height:40px;font-size:13px}

/* hero */
.hero{position:absolute;top:82px;left:0;width:1200px;height:633px;background:linear-gradient(90deg,#e9eef3 0%,#d3e0ea 40%,#8fa6bb 70%,#f1b45c 90%,#c9d6e2 100%)}
.hero-veil{position:absolute;inset:0;background:linear-gradient(90deg,rgba(240,244,248,.92) 0%,rgba(240,244,248,.6) 45%,rgba(240,244,248,0) 70%)}
.hero-title{position:absolute;left:70px;top:166px;font-size:50px;line-height:52px;font-weight:700;color:#34383d}
.hero-lead{position:absolute;left:72px;top:280px;width:460px;font-size:18px;line-height:26px;color:#3e4348}
.hero-cta{left:72px;top:396px;width:315px;height:63px;font-size:19px}

/* about */
.about-media{position:absolute;left:72px;top:820px;width:527px;height:372px;background:var(--white);box-shadow:0 2px 10px rgba(0,0,0,.12);padding:7px}
.about-photo{width:100%;height:100%;background:linear-gradient(135deg,#c4c8c6 0%,#6d625a 45%,#3a302b 100%);position:relative}
.play{position:absolute;left:50%;top:50%;width:82px;height:82px;margin:-41px 0 0 -41px;border-radius:50%;background:var(--orange);opacity:.9}
.about-title{position:absolute;left:734px;top:832px;font-size:47px;font-weight:700}
.about-text{position:absolute;left:734px;top:912px;width:385px;font-size:15.5px;line-height:24px;color:var(--text)}
.about-cta{left:734px;top:1121px;width:229px;height:56px;font-size:18px}

.section-title{position:absolute;left:0;width:1200px;text-align:center;font-size:47px;font-weight:700}

/* services */
.services{position:absolute;top:1367px;left:0;width:1200px;height:397px;display:flex}
.service{width:300px;height:397px;position:relative;color:var(--white);text-align:center}
.service+.service{border-left:1px solid rgba(255,255,255,.5)}
.service.blue{background:linear-gradient(180deg,#5db3df,#3f9dd0)}
.service.orange{background:linear-gradient(180deg,#f08a68,#ea6c48)}
.service h3{position:absolute;top:99px;width:100%;font-size:20px;font-weight:700}
.service p{position:absolute;top:140px;left:30px;width:240px;font-size:13.5px;line-height:21px;font-weight:300}
.service .more{position:absolute;left:66px;top:256px;width:169px;height:40px;border-radius:20px;background:var(--white);display:flex;align-items:center;justify-content:center;font-size:14px}
.service.blue .more{color:var(--blue)}
.service.orange .more{color:var(--orange)}

/* team */
.member{position:absolute;top:1960px;width:240px;text-align:center}
.avatar{width:125px;height:125px;border-radius:50%;margin:0 auto;background:linear-gradient(180deg,#d9d9d9,#7a7a7a)}
.member h4{margin-top:14px;font-size:19px;font-weight:400}
.member .role{margin-top:9px;font-size:13px;color:var(--muted);font-weight:300}
.social{margin-top:18px;display:flex;justify-content:center;gap:26px}
.social span{width:12px;height:12px;border-radius:50%;background:#cfcfcf}

/* map */
.map{position:absolute;top:2296px;left:0;width:1200px;height:314px;background:linear-gradient(90deg,#ecebe6 0%,#e6e4dd 45%,#9dc3ea 52%,#e8e6df 70%,#a9cdee 100%)}
.map-pin{position:absolute;left:562px;top:2446px;width:12px;height:12px;border-radius:50%;background:var(--orange)}
.map-label{position:absolute;left:593px;top:2427px;width:404px;height:45px;background:var(--white);border-radius:23px;box-shadow:0 2px 8px rgba(0,0,0,.15);display:flex;align-items:center;justify-content:center;font-size:12px;color:var(--ink)}

/* contact */
.contact-title{position:absolute;left:190px;top:2682px;font-size:32px;font-weight:700}
.contact-text{position:absolute;left:190px;top:2748px;width:310px;font-size:12px;line-height:23px;color:var(--text)}
.info-label{position:absolute;left:190px;font-size:8px;letter-spacing:1px;color:#b0b0b0}
.info-value{position:absolute;left:190px;font-size:12px;color:var(--ink)}
.field{position:absolute;background:var(--field);border:1px solid var(--line);font-size:12px;color:var(--muted);display:flex;align-items:center;gap:10px;padding-left:18px}
.field.area{align-items:flex-start;padding-top:12px}
.field svg{width:14px;height:14px;fill:#9aa3ad}
.send{left:612px;top:2917px;width:141px;height:40px;font-size:10px;letter-spacing:2px}

/* footer */
.site-footer{position:absolute;top:3041px;left:0;width:1200px;height:352px;background:var(--footer)}
.foot-col{position:absolute;top:75px}
.foot-col h5{font-size:10px;letter-spacing:2.5px;color:var(--white);font-weight:700}
.foot-col a{display:block;margin-top:19px;font-size:11.5px;color:var(--footer-text);text-decoration:none}
.foot-col a:first-of-type{margin-top:24px}
.newsletter{position:absolute;left:818px;top:107px;width:204px;height:40px;border-radius:20px;background:#3b3b3b;font-size:11px;color:var(--footer-text);display:flex;align-items:center;padding-left:22px}
.newsletter .go{position:absolute;right:0;top:3px;width:34px;height:34px;border-radius:50%;background:var(--orange);display:flex;align-items:center;justify-content:center}
.copyright{position:absolute;left:183px;top:277px;font-size:11.5px;color:var(--footer-text)}
</style>
</head>
<body>

<header class="site-header">
  <div class="brand"><span class="brand-dot"></span>Tavlin-Brokers</div>
  <nav class="main-nav">
    <a style="left:430px">HOME</a>
    <a style="left:533px">ABOUT US</a>
    <a style="left:664px">OUR SERVICES <svg width="9" height="6" viewBox="0 0 9 6"><path d="M1 1l3.5 3.5L8 1" stroke="#888" fill="none"/></svg></a>
    <a style="left:824px">OUR TEAM</a>
  </nav>
  <a class="btn nav-cta">CONTACT US</a>
</header>

<section class="hero" role="img" aria-label="Double exposure of an engineer holding a hard hat over an oil refinery">
  <div class="hero-veil"></div>
  <h1 class="hero-title">INSURANCE<br>BROKERAGE FIRM</h1>
  <p class="hero-lead">We Strive to make a difference in the market, bringing modernity and speed to our industry, still too bureaucratic, procedural and opaque uninitiated.</p>
  <a class="btn hero-cta">CONTACT US</a>
</section>

<section class="about">
  <div class="about-media">
    <div class="about-photo" role="img" aria-label="Video still of two colleagues reviewing a chart on a laptop">
      <div class="play"></div>
      <svg class="abs" style="left:50%;top:50%;margin:-14px 0 0 -9px" width="24" height="28" viewBox="0 0 24 28"><path d="M0 0L24 14L0 28Z" fill="#fff"/></svg>
    </div>
  </div>
  <h2 class="about-title">About Us</h2>
  <p class="about-text">Lorem ipsum dolor sit amet, consectetur adipiscing elit. Maecenas tempor, ante ut gravida malesuada, tortor ex molestie odio, non feugiat nisi lacus vitae nulla. Aliquam tempor gravida justo at tincidunt. Class aptent taciti sociosqu ad litora torquent per conubia nostra, per inceptos himenaeos. Nulla facilisis dolor sit amet mollis congue.</p>
  <a class="btn about-cta">LEARN MORE</a>
</section>

<h2 class="section-title" style="top:1272px">Our Services</h2>
<section class="services">
  <article class="service blue" role="img" aria-label="Hands sheltering a small house">
    <h3>LIABILITIES INSURANCE</h3>
    <p>Lorem ipsum dolor sit amet, consectetur adipiscing elit. Aliquam convallis in massa id aliquam. Cras nec iaculis augue, sed porttitor augue.</p>
    <span class="more">Learn More</span>
  </article>
  <article class="service orange" role="img" aria-label="Hands around a model car">
    <h3>AUTOMOBILE INSURANCE</h3>
    <p>Lorem ipsum dolor sit amet, consectetur adipiscing elit. Aliquam convallis in massa id aliquam. Cras nec iaculis augue, sed porttitor augue.</p>
    <span class="more">Learn More</span>
  </article>
  <article class="service blue" role="img" aria-label="Hands stacking blocks with health icons">
    <h3>CASUALTY INSURANCE</h3>
    <p>Lorem ipsum dolor sit amet, consectetur adipiscing elit. Aliquam convallis in massa id aliquam. Cras nec iaculis augue, sed porttitor augue.</p>
    <span class="more">Learn More</span>
  </article>
  <article class="service orange" role="img" aria-label="Coins wrapped in a rope">
    <h3>M&amp;T CREDIT INSURANCE</h3>
    <p>Lorem ipsum dolor sit amet, consectetur adipiscing elit. Aliquam convallis in massa id aliquam. Cras nec iaculis augue, sed porttitor augue.</p>
    <span class="more">Learn More</span>
  </article>
</section>

<h2 class="section-title" style="top:1842px">Our Team</h2>
<section class="team">
  <div class="member" style="left:162px"><div class="avatar" role="img" aria-label="Portrait of team member"></div><h4>Full Name Here</h4><div class="role">OCCUPATION</div><div class="social"><span></span><span></span></div></div>
  <div class="member" style="left:480px"><div class="avatar" role="img" aria-label="Portrait of team member"></div><h4>Full Name Here</h4><div class="role">OCCUPATION</div><div class="social"><span></span><span></span></div></div>
  <div class="member" style="left:798px"><div class="avatar" role="img" aria-label="Portrait of team member"></div><h4>Full Name Here</h4><div class="role">OCCUPATION</div><div class="social"><span></span><span></span></div></div>
</section>

<div class="map" role="img" aria-label="Street map around the office location in Luanda"></div>
<div class="map-pin"></div>
<div class="map-label">RUA DO KIMBUNDU 18/20, LUANDA, ANGOLA</div>

<section class="contact">
  <h2 class="contact-title">Contacts Us</h2>
  <p class="contact-text">Lorem ipsum dolor sit amet, consectetur adipiscing elit. Fusce sapien risus, congue vitae lectus a, lacinia posuere dui. Quisque sed viverra mauris.</p>
  <div class="info-label" style="top:2853px">ADDRESS:</div>
  <div class="info-value" style="top:2873px">Rua do Kimbundu 18/20, Luanda, Angola</div>
  <div class="info-label" style="top:2916px">PHONE:</div>
  <div class="info-value" style="top:2935px">+244 222 555010</div>

  <div class="field" style="left:612px;top:2691px;width:205px;height:38px"><svg viewBox="0 0 14 14"><circle cx="7" cy="4" r="3"/><path d="M1 14c0-4 3-6 6-6s6 2 6 6z"/></svg>Name</div>
  <div class="field" style="left:827px;top:2691px;width:207px;height:38px"><svg viewBox="0 0 14 14"><rect x="0" y="2" width="14" height="10"/></svg>E-mail</div>
  <div class="field area" style="left:612px;top:2743px;width:422px;height:157px">Your Message</div>
  <a class="btn send">SEND</a>
</section>

<footer class="site-footer">
  <div class="foot-col" style="left:183px"><h5>LEARN MORE</h5><a>Home</a><a>Services</a><a>Our Team</a><a>Testimonials</a></div>
  <div class="foot-col" style="left:395px"><h5>INFORMATION</h5><a>About Us</a><a>FAQs</a><a>Privacy Policy</a><a>Terms &amp; Conditions</a></div>
  <div class="foot-col" style="left:606px"><h5>GET IN TOUCH</h5><a>Contact Us</a><a>Customer Service</a></div>
  <div class="foot-col" style="left:816px"><h5>SUBSCRIBE TO NEWSLETTER</h5></div>
  <div class="newsletter">E-mail<span class="go"><svg width="14" height="10" viewBox="0 0 14 10"><rect x="0.5" y="0.5" width="13" height="9" fill="none" stroke="#fff"/><path d="M0.5 0.5L7 6L13.5 0.5" fill="none" stroke="#fff"/></svg></span></div>
  <div class="copyright">© 2019 Tavlin Brokers. All rights reserved.</div>
</footer>

</body>
</html>
```